International Film making Business needs the 5 Logos provided made into a POSTER Format

Design Task:
CREATE A POSTER DESIGN USING THE 5 LOGOS PROVIDED. The GLAD SKY VISTA LOGO should stand out from the others by being in the middle with the other 4 logos connected to it somehow.

The 5 Businesses already has their 5 Logos, all similar in design to each other.

GLAD SKY VISTA is the Main Logo that encompasses the other 4 Logos. So it must stand out more and it is like the Overall Business entity that incorporates the other 4 Logos.

What is required is that by using the 5 Logo designs provided, create a cool graphic artwork that somehow incorporates ALL of the 5 Logos - But having the GLAD SKY VISTA Logo at the forefront/most important/standing out the most.
- GLAD SKY VISTA will probably be bigger than the others
- and could be changed into 3D.

I have attached all 5 logos and a hand drawn example of how the GLAD SKY VISTAS could stand out from the rest.

THE DESIGNS OF THE LOGOS SHOULD NOT BE CHANGED (except the GLADSKYVISTA which can be 3D)

Please do not be restricted with the sample idea. Creativity is encouraged

DIMENSION: 3000 mm x 6000 mm
high resolution graphic

Logo Text

glad sky , glad sky reels, glad sky tales, glad sky groovy, GLAD SKY VISTAS

Requirements
Must have
• USE THE 5 LOGOS PROVIDED ONLY - Only GLAD SKY VISTA can be changed into 3D only
Nice to have
• Eye catching design, showing the Glad Sky Vista as the most powerful Logo that has the other 4 as subordinate companies
Should not have
• ANY CHANGE IN THE 5 LOGO DESIGNS (EXcept 3D for Glad Sky Vistas)

```html
<!DOCTYPE html>
<html lang="en">
<head>
<meta charset="utf-8">
<title>Glad Sky Vistas – Group Poster</title>
<link href="https://fonts.googleapis.com/css2?family=Cinzel:wght@600&family=Questrial&display=swap" rel="stylesheet">
<style>
  :root {
    --bg-edge: #c3c3c3;
    --bg-mid: #fbfbfb;
    --pole-dark: #8d8d8d;
    --pole-light: #d6d6d6;
    --sky-blue: #1d7fc4;
    --sky-navy: #2a4a9a;
    --tales-ink: #6a3aa0;
    --vista-gold: #b08a2e;
    --vista-pale: #efd9a0;
    --reels-ink: #1c1c1c;
    --reels-grey: #9a9a9a;
    --groovy-green: #2a9a1a;
    --groovy-deep: #0f6a12;
    --url-grey: #6b6b6b;
  }
  html, body {
    margin: 0;
    padding: 0;
    width: 682px;
    height: 1200px;
    overflow: hidden;
  }
  body {
    background: linear-gradient(to bottom, var(--bg-edge) 0%, var(--bg-mid) 48%, var(--bg-edge) 100%);
  }
  .poster {
    display: block;
    width: 682px;
    height: 1200px;
  }
  .wordmark {
    font-family: "Cinzel", serif;
    font-weight: 600;
    letter-spacing: 4px;
  }
  .wordmark--sky { fill: var(--sky-blue); }
  .wordmark--tales { fill: var(--tales-ink); }
  .wordmark--vista { fill: var(--vista-gold); }
  .wordmark--reels { fill: var(--reels-ink); }
  .wordmark--groovy { fill: var(--groovy-green); }
  .site-url {
    font-family: "Questrial", sans-serif;
    font-size: 25px;
    letter-spacing: 3px;
    fill: var(--url-grey);
  }
  .unit-outline {
    stroke-width: 7;
    stroke-linejoin: miter;
  }
  .badge {
    fill: none;
    stroke-width: 5;
  }
</style>
</head>
<body>
<svg class="poster" viewBox="165 127 1142 2301" preserveAspectRatio="xMidYMid meet" role="img" aria-label="Glad Sky Vistas group poster: five hexagon units branching from a central pole">
  <defs>
    <linearGradient id="bg-fill" gradientUnits="userSpaceOnUse" x1="0" y1="127" x2="0" y2="2428">
      <stop offset="0" stop-color="var(--bg-edge)"/>
      <stop offset="0.48" stop-color="var(--bg-mid)"/>
      <stop offset="1" stop-color="var(--bg-edge)"/>
    </linearGradient>
    <linearGradient id="pole-shade" x1="0" y1="0" x2="1" y2="0">
      <stop offset="0" stop-color="var(--pole-dark)"/>
      <stop offset="0.45" stop-color="var(--pole-light)"/>
      <stop offset="1" stop-color="var(--pole-dark)"/>
    </linearGradient>
    <linearGradient id="stroke-sky" x1="0" y1="0" x2="1" y2="1">
      <stop offset="0" stop-color="var(--sky-navy)"/>
      <stop offset="0.5" stop-color="var(--sky-blue)"/>
      <stop offset="1" stop-color="var(--sky-navy)"/>
    </linearGradient>
    <linearGradient id="stroke-tales" x1="0" y1="0" x2="0" y2="1">
      <stop offset="0" stop-color="#ff1a00"/>
      <stop offset="0.2" stop-color="#ffd400"/>
      <stop offset="0.42" stop-color="#f4ec00"/>
      <stop offset="0.6" stop-color="#1a3ec8"/>
      <stop offset="0.8" stop-color="#1a4aa0"/>
      <stop offset="1" stop-color="#2ad41a"/>
    </linearGradient>
    <linearGradient id="stroke-vista" x1="0" y1="0" x2="1" y2="1">
      <stop offset="0" stop-color="var(--vista-gold)"/>
      <stop offset="0.5" stop-color="var(--vista-pale)"/>
      <stop offset="1" stop-color="var(--vista-gold)"/>
    </linearGradient>
    <linearGradient id="stroke-reels" x1="0" y1="0" x2="1" y2="1">
      <stop offset="0" stop-color="var(--reels-ink)"/>
      <stop offset="0.5" stop-color="var(--reels-grey)"/>
      <stop offset="1" stop-color="var(--reels-ink)"/>
    </linearGradient>
    <linearGradient id="stroke-groovy" x1="0" y1="0" x2="1" y2="1">
      <stop offset="0" stop-color="var(--groovy-deep)"/>
      <stop offset="0.5" stop-color="#3cc41e"/>
      <stop offset="1" stop-color="var(--groovy-deep)"/>
    </linearGradient>
    <path id="unit-right" d="M873,525 L1080,410 L1268,520 L1268,765 L1075,872 L905,782 C870,765 840,780 838,820 L832,900 L735,955 L638,900 L638,790 L735,737 L775,760 C800,772 860,775 868,720 Z"/>
    <path id="unit-left" d="M597,783 L390,663 L203,772 L203,1015 L397,1125 L570,1035 C605,1020 632,1040 634,1080 L638,1155 L737,1210 L832,1155 L832,1045 L737,990 L680,1020 C650,1030 605,1020 600,975 Z"/>
  </defs>

  <rect class="backdrop" x="-2000" y="0" width="6000" height="3000" fill="url(#bg-fill)"/>

  <!-- central pole -->
  <g class="pole">
    <rect x="712" y="565" width="45" height="1780" rx="22" fill="url(#pole-shade)"/>
    <ellipse cx="734.5" cy="570" rx="22.5" ry="7" fill="#a9a9a9"/>
  </g>

  <!-- Glad Sky (main) -->
  <g class="unit unit--sky">
    <use href="#unit-right" class="unit-outline" fill="url(#bg-fill)" stroke="url(#stroke-sky)"/>
    <circle class="badge" cx="735" cy="846" r="42" stroke="var(--sky-blue)"/>
    <text class="wordmark wordmark--sky" x="937" y="652" font-size="88" textLength="266" lengthAdjust="spacingAndGlyphs">GLAD</text>
    <text class="wordmark wordmark--sky" x="937" y="736" font-size="88" textLength="248" lengthAdjust="spacingAndGlyphs">SKY</text>
  </g>

  <!-- Glad Sky Tales -->
  <g class="unit unit--tales">
    <use href="#unit-left" class="unit-outline" fill="url(#bg-fill)" stroke="url(#stroke-tales)"/>
    <circle class="badge" cx="735" cy="1100" r="42" stroke="var(--tales-ink)"/>
    <text class="wordmark wordmark--tales" x="240" y="900" font-size="56" textLength="312" lengthAdjust="spacingAndGlyphs">GLAD SKY</text>
    <text class="wordmark wordmark--tales" x="240" y="960" font-size="66" textLength="318" lengthAdjust="spacingAndGlyphs">TALES</text>
  </g>

  <!-- Glad Sky Vistas -->
  <g class="unit unit--vista" transform="translate(0 525)">
    <use href="#unit-right" class="unit-outline" fill="url(#bg-fill)" stroke="url(#stroke-vista)"/>
    <circle class="badge" cx="735" cy="846" r="42" stroke="var(--vista-gold)"/>
  </g>
  <g class="wordmark-group">
    <text class="wordmark wordmark--vista" x="900" y="1152" font-size="58" textLength="332" lengthAdjust="spacingAndGlyphs">GLAD SKY</text>
    <text class="wordmark wordmark--vista" x="900" y="1210" font-size="58" textLength="332" lengthAdjust="spacingAndGlyphs">VISTAS</text>
    <text class="site-url" x="900" y="1238" textLength="332" lengthAdjust="spacingAndGlyphs">gladskyvistas.com.au</text>
  </g>

  <!-- Glad Sky Reels -->
  <g class="unit unit--reels" transform="translate(0 537)">
    <use href="#unit-left" class="unit-outline" fill="url(#bg-fill)" stroke="url(#stroke-reels)"/>
    <circle class="badge" cx="735" cy="1100" r="42" stroke="var(--reels-ink)"/>
  </g>
  <text class="wordmark wordmark--reels" x="248" y="1416" font-size="50" textLength="290" lengthAdjust="spacingAndGlyphs">GLAD SKY</text>
  <text class="wordmark wordmark--reels" x="246" y="1500" font-size="88" textLength="294" lengthAdjust="spacingAndGlyphs">REELS</text>

  <!-- Glad Sky Groovy -->
  <g class="unit unit--groovy" transform="translate(0 1042)">
    <use href="#unit-right" class="unit-outline" fill="url(#bg-fill)" stroke="url(#stroke-groovy)"/>
    <circle class="badge" cx="735" cy="846" r="42" stroke="var(--groovy-green)"/>
  </g>
  <text class="wordmark wordmark--groovy" x="902" y="1672" font-size="54" textLength="304" lengthAdjust="spacingAndGlyphs">GLAD SKY</text>
  <text class="wordmark wordmark--groovy" x="902" y="1746" font-size="78" textLength="304" lengthAdjust="spacingAndGlyphs">GROOVY</text>
</svg>
</body>
</html>
```